School learning environment project dashboard

We have an online learning enviroment for schools (12 / 18 year). Within this enviroment students work on projects.

Attached we have a setup we have created for a project, but we are looking for more ideas to make this even better, more sexy and still keep it functional for teachers and students.

The attached files show one dashboard we have. This dashboard holds the roadmap for the student, upcoming appointments, latest messages and the main documents the student is working on.

Target Market(s)

schools

Number of Pages Required

1 page

Font styles to use
Sans Serif

```html
<!DOCTYPE html>
<html lang="en">
<head>
<meta charset="utf-8">
<title>Learnpath – Student Project Dashboard</title>
<link href="https://fonts.googleapis.com/css2?family=Lato:wght@400;700;900&display=swap" rel="stylesheet">
<style>
:root{
  --stage:#68afd4;
  --brand:#1a86cf;
  --brand-dark:#1560a8;
  --popup:#1a78c0;
  --page:#eff0f2;
  --panel:#f3f3f3;
  --card:#ffffff;
  --ink:#2b2b2b;
  --muted:#555;
  --link:#1a78c0;
  --orange:#f0a21a;
  --submit:#fdab1c;
  --green:#3cb43c;
  --red:#d92020;
  --sky:#3ca6e2;
  --sun:#f9c900;
  --violet:#c84fe0;
  --teal:#22a7e0;
}
*{box-sizing:border-box;margin:0;padding:0}
html,body{width:1200px;height:418px;overflow:hidden}
body{background:var(--stage);font-family:"Lato",Arial,sans-serif;color:var(--ink);position:relative}
.screen{position:absolute;top:23.3px;width:781px;height:780px;background:var(--page);transform:scale(.4658);transform-origin:0 0;overflow:hidden}
.screen--a{left:20px}.screen--b{left:418.3px}.screen--c{left:816.2px}
.abs{position:absolute}
/* top bar */
.topbar{position:absolute;left:0;top:0;width:781px;height:42px;background:var(--brand);color:#fff}
.brand{position:absolute;left:24px;top:12px;font-weight:900;font-size:15px;display:flex;align-items:center;gap:6px}
.brand i{width:10px;height:10px;background:#fff;display:block}
.user{position:absolute;left:508px;top:7px;display:flex;align-items:center;gap:6px}
.avatar{width:27px;height:27px;border-radius:50%;background:radial-gradient(circle at 50% 40%,#d9b49a,#6b5548);border:2px solid #fff}
.user small{display:block;font-size:8px;line-height:9px}
.user b{display:block;font-size:10px;line-height:11px}
.bell{position:absolute;left:645px;top:14px}
.bell span{position:absolute;left:9px;top:-5px;width:10px;height:10px;border-radius:50%;background:var(--sun);color:#333;font-size:7px;text-align:center;line-height:10px}
.logout{position:absolute;left:680px;top:15px;font-size:10px;display:flex;gap:4px;align-items:center}
/* sidebar */
.sidebar{position:absolute;left:0;top:55px;width:147px;height:653px;background:var(--card)}
.nav{list-style:none}
.nav li{height:35.5px;border-bottom:1px solid #ececec;display:flex;align-items:center;padding-left:25px;gap:11px;font-size:9px;font-weight:700;letter-spacing:.2px}
.nav svg{width:10px;height:10px;fill:var(--brand-dark)}
/* hero */
.hero{position:absolute;left:157px;top:55px;width:576px;height:95px;border-radius:6px;background:linear-gradient(100deg,#3c3f44 0%,#55575a 45%,#2f3236 70%,#6c5f55 100%);color:#fff;padding:16px 16px}
.hero h1{font-size:16px;font-weight:700}
.crumbs{font-size:9px;margin-top:9px}
.hide{font-size:9px;margin-top:13px;display:flex;gap:8px;align-items:center}
/* main */
.main{position:absolute;left:157px;top:162px;width:576px;height:546px;background:var(--card);border-radius:4px}
.tabs{position:absolute;left:9px;top:10px;display:flex;font-size:9px}
.tabs span{padding:4px 8px 7px;margin-right:13px}
.tabs .on{color:var(--link);font-weight:700;border-bottom:2px solid var(--link)}
.tools{position:absolute;right:12px;top:12px;display:flex;gap:11px}
.tools svg{width:11px;height:11px;fill:var(--orange)}
.box{position:absolute;background:var(--panel);border-radius:5px}
.box h2{position:absolute;left:13px;top:14px;font-size:13px;font-weight:400;color:#222}
.viewall{position:absolute;right:13px;top:17px;font-size:7.5px;color:var(--link);text-decoration:underline}
.arrows{position:absolute;right:13px;top:15px;display:flex;gap:3px}
.arrows i{width:10px;height:10px;border-radius:50%;display:block}
.step{position:absolute;top:45px;width:60px;text-align:center}
.dot{width:40px;height:40px;border-radius:50%;margin:0 auto;color:#fff;font-size:12px;font-weight:700;line-height:40px;position:relative}
.step small{display:block;font-size:7.5px;margin-top:6px}
.badge{position:absolute;right:-9px;top:-1px;width:11px;height:11px}
.row{position:absolute;background:var(--card);border-radius:3px;display:flex;align-items:center;padding:0 11px;font-size:8.5px}
.row .ico{width:9px;height:9px;fill:var(--brand-dark);margin-right:13px}
.row .acts{margin-left:auto;display:flex;gap:12px}
.row .acts svg{width:10px;height:10px;fill:var(--orange)}
.row b{font-weight:700}
.row .sub{font-size:8px}
.row .state{margin-left:auto;width:11px;height:11px}
.empty{color:var(--link);font-size:8px}
.author{position:absolute;left:15px;top:40px;font-size:8.5px;color:var(--link);font-weight:700}
.date{position:absolute;right:13px;top:40px;font-size:8.5px}
.thumb{margin-left:auto;width:31px;height:31px;background:linear-gradient(#e7e2dc,#a68a78)}
.chat{position:absolute;left:740px;top:700px;width:34px;height:34px;border-radius:50%;background:var(--brand);display:flex;align-items:center;justify-content:center}
.footer{position:absolute;left:0;width:781px;top:738px;text-align:center;font-size:8.5px;padding-right:170px}
.scale{position:absolute;left:759px;top:758px;font-size:8px;color:var(--link)}
/* message popup */
.popup{position:absolute;left:517px;top:447px;width:216px;height:258px;background:var(--popup);border-radius:6px;border:2px solid #bfe0f5;color:#fff;padding:0 10px}
.popup h3{font-size:10.5px;font-weight:400;margin:14px 0 13px 5px}
.popup .close{position:absolute;right:10px;top:14px;width:10px;height:10px;border:1px solid #fff}
.field{background:#fff;color:#444;border-radius:15px;height:30px;font-size:8px;padding:0 13px;line-height:30px;margin-bottom:7px}
.field--area{height:88px;border-radius:12px;line-height:1;padding-top:11px}
.submit{background:var(--submit);border-radius:15px;height:29px;text-align:center;line-height:29px;font-weight:700;font-size:10.5px;margin-top:-1px}
</style>
</head>
<body>
<svg width="0" height="0" style="position:absolute">
  <defs>
    <symbol id="i-down" viewBox="0 0 10 10"><path d="M4 0h2v4h2L5 7 2 4h2zM0 8h10v2H0z"/></symbol>
    <symbol id="i-up" viewBox="0 0 10 10"><path d="M5 0l3 3H6v4H4V3H2zM0 8h10v2H0z"/></symbol>
    <symbol id="i-folder" viewBox="0 0 10 10"><path d="M0 2h4l1 1h5v6H0z"/></symbol>
    <symbol id="i-eye" viewBox="0 0 10 10"><path d="M5 2C2 2 0 5 0 5s2 3 5 3 5-3 5-3-2-3-5-3zm0 5a2 2 0 110-4 2 2 0 010 4z"/></symbol>
    <symbol id="i-doc" viewBox="0 0 10 10"><path d="M1 0h5l3 3v7H1z"/></symbol>
    <symbol id="i-chart" viewBox="0 0 10 10"><path d="M0 0h1v9h9v1H0zM2 7l3-3 2 2 3-4v2L7 8 5 6 3 8z"/></symbol>
    <symbol id="i-pie" viewBox="0 0 10 10"><path d="M4 1a4.5 4.5 0 105 5H4z"/><path d="M5 0v5h5a5 5 0 00-5-5z"/></symbol>
    <symbol id="i-tick" viewBox="0 0 12 12"><circle cx="6" cy="6" r="6" fill="#3cb43c"/><path d="M3 6l2 2 4-4" stroke="#fff" stroke-width="1.6" fill="none"/></symbol>
    <symbol id="i-edit" viewBox="0 0 12 12"><rect width="12" height="12" fill="#22a7e0"/><path d="M3 9l1-3 4-4 2 2-4 4z" fill="#fff"/></symbol>
    <symbol id="i-chat" viewBox="0 0 12 12"><rect y="1" width="12" height="9" rx="1" fill="#f0a21a"/><circle cx="3.5" cy="5.5" r="1" fill="#fff"/><circle cx="6" cy="5.5" r="1" fill="#fff"/><circle cx="8.5" cy="5.5" r="1" fill="#fff"/></symbol>
    <symbol id="i-cross" viewBox="0 0 12 12"><rect width="12" height="12" fill="#d92020"/><path d="M3 3l6 6M9 3l-6 6" stroke="#fff" stroke-width="1.6"/></symbol>
    <symbol id="i-basket" viewBox="0 0 10 10"><path d="M0 3h10l-1 6H1zM3 3l2-3 2 3"/></symbol>
    <symbol id="i-pencil" viewBox="0 0 10 10"><path d="M0 10l1-3 6-6 2 2-6 6z"/></symbol>
    <symbol id="i-lock" viewBox="0 0 10 10"><path d="M2 4V3a3 3 0 016 0v1h1v6H1V4zm1.5 0h3V3a1.5 1.5 0 00-3 0z"/></symbol>
    <symbol id="i-square" viewBox="0 0 10 10"><rect x="1" y="1" width="8" height="8" rx="2"/></symbol>
    <symbol id="i-bubble" viewBox="0 0 16 16"><path d="M8 2C4 2 1 4.5 1 7.5c0 1.6.9 3 2.3 4L2.5 14l3.2-1.6c.7.2 1.5.3 2.3.3 4 0 7-2.5 7-5.5S12 2 8 2z" fill="#fff"/><circle cx="5" cy="7.5" r="1" fill="#1a86cf"/><circle cx="8" cy="7.5" r="1" fill="#1a86cf"/><circle cx="11" cy="7.5" r="1" fill="#1a86cf"/></symbol>
  </defs>
</svg>

<!-- ===== Screen A : full dashboard ===== -->
<section class="screen screen--a">
  <header class="topbar">
    <div class="brand"><i></i>Learnpath</div>
    <div class="user"><div class="avatar" role="img" aria-label="Profile photo of the student"></div><div><small>Welcome</small><b>Marco Delvane</b></div></div>
    <div class="bell"><svg width="11" height="12" viewBox="0 0 10 11"><path d="M5 0a3.5 3.5 0 00-3.5 3.5V7L0 8.5V9h10v-.5L8.5 7V3.5A3.5 3.5 0 005 0zM4 10h2a1 1 0 01-2 0z" fill="#fff"/></svg><span>0</span></div>
    <div class="logout"><svg width="9" height="9" viewBox="0 0 10 10"><path d="M0 1h4v1H1v6h3v1H0zM6 2l3 3-3 3V6H3V4h3z" fill="#fff"/></svg>Log Out</div>
  </header>
  <aside class="sidebar"><ul class="nav">
    <li><svg><use href="#i-square"/></svg>DASHBOARD</li><li><svg><use href="#i-square"/></svg>PROJECTS</li><li><svg><use href="#i-square"/></svg>ONLINE</li><li><svg><use href="#i-square"/></svg>PROFILES</li><li><svg><use href="#i-square"/></svg>APP</li><li><svg><use href="#i-square"/></svg>OPPORTUNITIES</li><li><svg><use href="#i-square"/></svg>HELP</li><li><svg><use href="#i-square"/></svg>TOOLS</li>
  </ul></aside>
  <div class="hero" role="img" aria-label="Banner photo of hands typing on a laptop">
    <h1>Example</h1>
    <p class="crumbs">Dashboard &nbsp;/&nbsp; Projects &nbsp;/&nbsp; Profile Paper 2020-2021 &nbsp;/&nbsp; Example</p>
    <p class="hide"><svg width="10" height="10" viewBox="0 0 10 10"><circle cx="5" cy="5" r="5" fill="#fff"/><path d="M6 2.5L3.5 5 6 7.5" stroke="#333" stroke-width="1.4" fill="none"/></svg>Hide Menu</p>
  </div>
  <main class="main">
    <nav class="tabs"><span class="on">Progress</span><span>Tools</span><span>Messages</span></nav>
    <div class="tools"><svg><use href="#i-basket"/></svg><svg><use href="#i-pencil"/></svg><svg><use href="#i-lock"/></svg></div>
    <div class="box" style="left:9px;top:43px;width:557px;height:111px">
      <h2>Timeline</h2>
      <div class="arrows"><i style="background:#5aa9e0"></i><i style="background:var(--brand-dark)"></i></div>
      <div class="step" style="left:10px"><div class="dot" style="background:var(--sky)">01<svg class="badge"><use href="#i-tick"/></svg></div><small>00 Month</small></div>
      <div class="step" style="left:106px"><div class="dot" style="background:var(--sky)">02<svg class="badge"><use href="#i-tick"/></svg></div><small>00 Month</small></div>
      <div class="step" style="left:202px"><div class="dot" style="background:var(--sky)">03<svg class="badge"><use href="#i-tick"/></svg></div><small>00 Month</small></div>
      <div class="step" style="left:298px"><div class="dot" style="background:var(--brand-dark)">04<svg class="badge"><use href="#i-edit"/></svg></div><small>00 Month</small></div>
      <div class="step" style="left:393px"><div class="dot" style="background:var(--sun)">05<svg class="badge"><use href="#i-chat"/></svg></div><small>00 Month</small></div>
      <div class="step" style="left:489px"><div class="dot" style="background:var(--violet)">06<svg class="badge"><use href="#i-cross"/></svg></div><small>00 Month</small></div>
    </div>
    <div class="box" style="left:9px;top:162px;width:273px;height:211px">
      <h2>Documents</h2>
      <div class="row" style="left:12px;top:42px;width:249px;height:44px"><svg class="ico"><use href="#i-doc"/></svg>Paper<span class="acts"><svg><use href="#i-down"/></svg><svg><use href="#i-up"/></svg><svg><use href="#i-folder"/></svg></span></div>
      <div class="row" style="left:12px;top:99px;width:249px;height:43px"><svg class="ico"><use href="#i-chart"/></svg>Plan of Action<span class="acts"><svg><use href="#i-eye"/></svg><svg><use href="#i-up"/></svg><svg><use href="#i-folder"/></svg></span></div>
      <div class="row" style="left:12px;top:155px;width:249px;height:43px"><svg class="ico"><use href="#i-pie"/></svg>Powerpoint<span class="acts"><svg><use href="#i-up"/></svg><svg><use href="#i-folder"/></svg></span></div>
    </div>
    <div class="box" style="left:294px;top:162px;width:272px;height:211px">
      <h2>Upcomming Appointments</h2><span class="viewall">View All &gt;&gt;</span>
      <div class="row" style="left:12px;top:42px;width:248px;height:44px"><div><b>Submitting research proposal</b><div class="sub">00 Month</div></div><svg class="state"><use href="#i-tick"/></svg></div>
      <div class="row" style="left:12px;top:99px;width:248px;height:43px"><div><b>Example</b><div class="sub">00 Month</div></div><svg class="state"><use href="#i-chat"/></svg></div>
      <div class="row" style="left:12px;top:155px;width:248px;height:43px"><div><b>Evaluation</b><div class="sub">00 Month</div></div><svg class="state"><use href="#i-cross"/></svg></div>
    </div>
    <div class="box" style="left:294px;top:382px;width:272px;height:150px">
      <h2>Recent Posts</h2><span class="viewall">View All &gt;&gt;</span>
      <span class="author">Jonas Verbeek</span><span class="date">4-02-2021 at 19:39</span>
      <div class="row" style="left:12px;top:60px;width:248px;height:43px">Example message<div class="thumb" role="img" aria-label="Portrait of the post author"></div></div>
    </div>
  </main>
  <div class="chat"><svg width="18" height="18"><use href="#i-bubble"/></svg></div>
  <p class="footer">Copyright © 2021 Learnpath All rights reserved</p>
  <span class="scale">x10</span>
</section>

<!-- ===== Screen B : leave message open ===== -->
<section class="screen screen--b">
  <header class="topbar">
    <div class="brand"><i></i>Learnpath</div>
    <div class="user"><div class="avatar" role="img" aria-label="Profile photo of the student"></div><div><small>Welcome</small><b>Marco Delvane</b></div></div>
    <div class="bell"><svg width="11" height="12" viewBox="0 0 10 11"><path d="M5 0a3.5 3.5 0 00-3.5 3.5V7L0 8.5V9h10v-.5L8.5 7V3.5A3.5 3.5 0 005 0zM4 10h2a1 1 0 01-2 0z" fill="#fff"/></svg><span>0</span></div>
    <div class="logout"><svg width="9" height="9" viewBox="0 0 10 10"><path d="M0 1h4v1H1v6h3v1H0zM6 2l3 3-3 3V6H3V4h3z" fill="#fff"/></svg>Log Out</div>
  </header>
  <aside class="sidebar"><ul class="nav">
    <li><svg><use href="#i-square"/></svg>DASHBOARD</li><li><svg><use href="#i-square"/></svg>PROJECTS</li><li><svg><use href="#i-square"/></svg>ONLINE</li><li><svg><use href="#i-square"/></svg>PROFILES</li><li><svg><use href="#i-square"/></svg>APP</li><li><svg><use href="#i-square"/></svg>OPPORTUNITIES</li><li><svg><use href="#i-square"/></svg>HELP</li><li><svg><use href="#i-square"/></svg>TOOLS</li>
  </ul></aside>
  <div class="hero" role="img" aria-label="Banner photo of hands typing on a laptop">
    <h1>Example</h1>
    <p class="crumbs">Dashboard &nbsp;/&nbsp; Projects &nbsp;/&nbsp; Profile Paper 2020-2021 &nbsp;/&nbsp; Example</p>
    <p class="hide"><svg width="10" height="10" viewBox="0 0 10 10"><circle cx="5" cy="5" r="5" fill="#fff"/><path d="M6 2.5L3.5 5 6 7.5" stroke="#333" stroke-width="1.4" fill="none"/></svg>Hide Menu</p>
  </div>
  <main class="main">
    <nav class="tabs"><span class="on">Progress</span><span>Tools</span><span>Messages</span></nav>
    <div class="tools"><svg><use href="#i-basket"/></svg><svg><use href="#i-pencil"/></svg><svg><use href="#i-lock"/></svg></div>
    <div class="box" style="left:9px;top:43px;width:557px;height:111px">
      <h2>Timeline</h2>
      <div class="arrows"><i style="background:#5aa9e0"></i><i style="background:var(--brand-dark)"></i></div>
      <div class="step" style="left:10px"><div class="dot" style="background:var(--sky)">01<svg class="badge"><use href="#i-tick"/></svg></div><small>00 Month</small></div>
      <div class="step" style="left:106px"><div class="dot" style="background:var(--sky)">02<svg class="badge"><use href="#i-tick"/></svg></div><small>00 Month</small></div>
      <div class="step" style="left:202px"><div class="dot" style="background:var(--sky)">03<svg class="badge"><use href="#i-tick"/></svg></div><small>00 Month</small></div>
      <div class="step" style="left:298px"><div class="dot" style="background:var(--brand-dark)">04<svg class="badge"><use href="#i-edit"/></svg></div><small>00 Month</small></div>
      <div class="step" style="left:393px"><div class="dot" style="background:var(--sun)">05<svg class="badge"><use href="#i-chat"/></svg></div><small>00 Month</small></div>
      <div class="step" style="left:489px"><div class="dot" style="background:var(--violet)">06<svg class="badge"><use href="#i-cross"/></svg></div><small>00 Month</small></div>
    </div>
    <div class="box" style="left:9px;top:162px;width:273px;height:211px">
      <h2>Documents</h2>
      <div class="row" style="left:12px;top:42px;width:249px;height:44px"><svg class="ico"><use href="#i-doc"/></svg>Paper<span class="acts"><svg><use href="#i-down"/></svg><svg><use href="#i-up"/></svg><svg><use href="#i-folder"/></svg></span></div>
      <div class="row" style="left:12px;top:99px;width:249px;height:43px"><svg class="ico"><use href="#i-chart"/></svg>Plan of Action<span class="acts"><svg><use href="#i-eye"/></svg><svg><use href="#i-up"/></svg><svg><use href="#i-folder"/></svg></span></div>
      <div class="row" style="left:12px;top:155px;width:249px;height:43px"><svg class="ico"><use href="#i-pie"/></svg>Powerpoint<span class="acts"><svg><use href="#i-up"/></svg><svg><use href="#i-folder"/></svg></span></div>
    </div>
    <div class="box" style="left:294px;top:162px;width:272px;height:211px">
      <h2>Upcomming Appointments</h2><span class="viewall">View All &gt;&gt;</span>
      <div class="row" style="left:12px;top:42px;width:248px;height:44px"><div><b>Submitting research proposal</b><div class="sub">00 Month</div></div><svg class="state"><use href="#i-tick"/></svg></div>
      <div class="row" style="left:12px;top:99px;width:248px;height:43px"><div><b>Example</b><div class="sub">00 Month</div></div><svg class="state"><use href="#i-chat"/></svg></div>
      <div class="row" style="left:12px;top:155px;width:248px;height:43px"><div><b>Evaluation</b><div class="sub">00 Month</div></div><svg class="state"><use href="#i-cross"/></svg></div>
    </div>
    <div class="box" style="left:294px;top:382px;width:272px;height:150px">
      <h2>Recent Posts</h2><span class="viewall">View All &gt;&gt;</span>
      <span class="author">Jonas Verbeek</span><span class="date">4-02-2021 at 19:39</span>
      <div class="row" style="left:12px;top:60px;width:248px;height:43px">Example message<div class="thumb" role="img" aria-label="Portrait of the post author"></div></div>
    </div>
  </main>
  <form class="popup">
    <h3>Leave Message</h3><span class="close"></span>
    <div class="field">Name (Required)</div>
    <div class="field">Email Address (Required)</div>
    <div class="field field--area">Message</div>
    <div class="submit">Submit</div>
  </form>
  <div class="chat"><svg width="18" height="18"><use href="#i-bubble"/></svg></div>
  <p class="footer">Copyright © 2021 Learnpath All rights reserved</p>
  <span class="scale">x10</span>
</section>

<!-- ===== Screen C : empty states ===== -->
<section class="screen screen--c">
  <header class="topbar">
    <div class="brand"><i></i>Learnpath</div>
    <div class="user"><div class="avatar" role="img" aria-label="Profile photo of the student"></div><div><small>Welcome</small><b>Marco Delvane</b></div></div>
    <div class="bell"><svg width="11" height="12" viewBox="0 0 10 11"><path d="M5 0a3.5 3.5 0 00-3.5 3.5V7L0 8.5V9h10v-.5L8.5 7V3.5A3.5 3.5 0 005 0zM4 10h2a1 1 0 01-2 0z" fill="#fff"/></svg><span>0</span></div>
    <div class="logout"><svg width="9" height="9" viewBox="0 0 10 10"><path d="M0 1h4v1H1v6h3v1H0zM6 2l3 3-3 3V6H3V4h3z" fill="#fff"/></svg>Log Out</div>
  </header>
  <aside class="sidebar"><ul class="nav">
    <li><svg><use href="#i-square"/></svg>DASHBOARD</li><li><svg><use href="#i-square"/></svg>PROJECTS</li><li><svg><use href="#i-square"/></svg>ONLINE</li><li><svg><use href="#i-square"/></svg>PROFILES</li><li><svg><use href="#i-square"/></svg>APP</li><li><svg><use href="#i-square"/></svg>OPPORTUNITIES</li><li><svg><use href="#i-square"/></svg>HELP</li><li><svg><use href="#i-square"/></svg>TOOLS</li>
  </ul></aside>
  <div class="hero" role="img" aria-label="Banner photo of hands typing on a laptop">
    <h1>Example</h1>
    <p class="crumbs">Dashboard &nbsp;/&nbsp; Projects &nbsp;/&nbsp; Profile Paper 2020-2021 &nbsp;/&nbsp; Example</p>
    <p class="hide"><svg width="10" height="10" viewBox="0 0 10 10"><circle cx="5" cy="5" r="5" fill="#fff"/><path d="M6 2.5L3.5 5 6 7.5" stroke="#333" stroke-width="1.4" fill="none"/></svg>Hide Menu</p>
  </div>
  <main class="main">
    <nav class="tabs"><span class="on">Progress</span><span>Tools</span><span>Messages</span></nav>
    <div class="tools"><svg><use href="#i-basket"/></svg><svg><use href="#i-pencil"/></svg><svg><use href="#i-lock"/></svg></div>
    <div class="box" style="left:9px;top:43px;width:557px;height:111px">
      <h2>Timeline</h2>
      <div class="arrows"><i style="background:#5aa9e0"></i><i style="background:var(--brand-dark)"></i></div>
      <div class="step" style="left:10px"><div class="dot" style="background:var(--sky)">01<svg class="badge"><use href="#i-tick"/></svg></div><small>00 Month</small></div>
      <div class="step" style="left:106px"><div class="dot" style="background:var(--sky)">02<svg class="badge"><use href="#i-tick"/></svg></div><small>00 Month</small></div>
      <div class="step" style="left:202px"><div class="dot" style="background:var(--sky)">03<svg class="badge"><use href="#i-tick"/></svg></div><small>00 Month</small></div>
      <div class="step" style="left:298px"><div class="dot" style="background:var(--brand-dark)">04<svg class="badge"><use href="#i-edit"/></svg></div><small>00 Month</small></div>
      <div class="step" style="left:393px"><div class="dot" style="background:var(--sun)">05<svg class="badge"><use href="#i-chat"/></svg></div><small>00 Month</small></div>
      <div class="step" style="left:489px"><div class="dot" style="background:var(--violet)">06<svg class="badge"><use href="#i-cross"/></svg></div><small>00 Month</small></div>
    </div>
    <div class="box" style="left:9px;top:162px;width:273px;height:211px">
      <h2>Documents</h2>
      <div class="row" style="left:12px;top:42px;width:249px;height:44px"><svg class="ico"><use href="#i-doc"/></svg>Paper<span class="acts"><svg><use href="#i-down"/></svg><svg><use href="#i-up"/></svg><svg><use href="#i-folder"/></svg></span></div>
      <div class="row" style="left:12px;top:99px;width:249px;height:43px"><svg class="ico"><use href="#i-chart"/></svg>Plan of Action<span class="acts"><svg><use href="#i-eye"/></svg><svg><use href="#i-up"/></svg><svg><use href="#i-folder"/></svg></span></div>
      <div class="row" style="left:12px;top:155px;width:249px;height:43px"><svg class="ico"><use href="#i-pie"/></svg>Powerpoint<span class="acts"><svg><use href="#i-up"/></svg><svg><use href="#i-folder"/></svg></span></div>
    </div>
    <div class="box" style="left:294px;top:162px;width:272px;height:100px">
      <h2>Upcomming Appointments</h2><span class="viewall">View All &gt;&gt;</span>
      <div class="row empty" style="left:12px;top:42px;width:248px;height:44px">No appointment to show you at the moment</div>
    </div>
    <div class="box" style="left:294px;top:275px;width:272px;height:98px">
      <h2>Recent Posts</h2><span class="viewall">View All &gt;&gt;</span>
      <div class="row empty" style="left:12px;top:41px;width:248px;height:44px">No message to show you at the moment</div>
    </div>
  </main>
  <div class="chat"><svg width="18" height="18"><use href="#i-bubble"/></svg></div>
  <p class="footer">Copyright © 2021 Learnpath All rights reserved</p>
  <span class="scale">x10</span>
</section>
</body>
</html>
```